Point of Sale Systems Web Design Project

I need a complete redesign of my existing website. I sell point of sale systems and need to seamlessly combine the features, products and services of several companies I represent. The current site is at www.tillgrovehub.com. The new site will be rebranded as www.VendaloFlo.com. I will be adding products from www.quillpoint.com, www.brenvale.com, www.dashkettle.com as well as other similar products and services such as http://orbanfield.com/homepage_USA.html

The new tag line will be:
Electronic Payment Systems Made FLO!
Updates

I have made a change to the website name. The new name will be VendaloFlo.com. I look forward to seeing the designs. Please see http://www.tovra.com.au/index.html for the inspiration behind the new name. I am also going to increase the budget for this project. Thank you

Target Market(s)

These are products and services for business owners. We provide Credit Card Processing Equipment and Processing Services to Retail, Restaurant, Home-based, and Internet businesses.

Industry/Entity Type

Electronic

Requirements
Must have
• Visitors need to be able to view video demos and download PDF documents. Site should be easy to update with new products or services.
Nice to have
• Designs I like: http://www.greyloftworks.com, http://www.pinewhistlegoods.com, http://www.lattiscobridge.com/

```html
<!DOCTYPE html>
<html lang="en">
<head>
<meta charset="utf-8">
<title>VendaloFlo.com – POS Technology, Systems And Solutions</title>
<link rel="stylesheet" href="https://fonts.googleapis.com/css2?family=Didact+Gothic&family=Open+Sans:wght@400;600&display=swap">
<style>
:root{
  --page:#ffffff;
  --band:#e4e4e4;
  --band-dark:#d6d6d6;
  --blue:#2b7bbd;
  --ink:#222222;
  --muted:#555555;
  --panel-dark:#5e5e5e;
  --panel-light:#e6e6e6;
  --btn:#a9a9a9;
  --red:#c0392b;
  --line:#cfcfcf;
}
*{box-sizing:border-box;margin:0;padding:0}
html,body{width:1149px;height:1200px;overflow:hidden}
body{background:var(--page);font-family:"Open Sans",Arial,sans-serif;color:var(--ink);position:relative}
.abs{position:absolute}

/* header */
.site-header{left:0;top:0;width:1149px;height:118px;background:var(--band)}
.brand{left:33px;top:52px;font-family:"Didact Gothic",sans-serif;font-size:34px;color:var(--blue);display:flex;align-items:center;gap:10px}
.brand-dot{width:14px;height:14px;border-radius:50%;background:var(--blue)}
.phone{right:24px;top:20px;font-family:"Didact Gothic",sans-serif;font-size:28px;color:var(--blue)}
.main-nav{left:420px;top:68px;display:flex}
.main-nav a{display:block;width:129px;text-align:center;font-family:"Didact Gothic",sans-serif;font-size:19px;color:var(--ink);text-decoration:none;border-left:1px solid #bfbfbf;line-height:36px}
.main-nav a:first-child{border-left:none;width:92px;text-align:left;padding-left:22px}

/* hero */
.hero-image{left:20px;top:182px;width:370px;height:230px;border-radius:8px;background:linear-gradient(160deg,#3c4a5e,#8a9bb0 55%,#b9a673)}
.hero-panel{left:420px;top:148px;width:709px;height:312px;border-left:2px solid var(--line);border-bottom:2px solid var(--line);border-radius:0 0 0 10px}
.hero-title{left:448px;top:164px;font-family:"Didact Gothic",sans-serif;font-size:38px;color:var(--blue);font-weight:400}
.hero-copy{left:448px;top:225px;width:675px;font-size:15.4px;line-height:20.5px;color:var(--ink)}
.btn{height:41px;background:var(--btn);color:#fff;font-family:"Didact Gothic",sans-serif;border-radius:3px;box-shadow:2px 2px 3px rgba(0,0,0,.25);display:flex;align-items:center}
.btn-terminal{left:449px;top:401px;width:153px;font-size:18px;padding-left:10px}
.btn-process{left:609px;top:401px;width:152px;font-size:12px;padding-left:8px;justify-content:space-between;padding-right:8px}
.pdf-link{left:1044px;top:392px;width:72px;text-align:center;font-size:12px;color:var(--ink)}
.divider{height:4px;background:linear-gradient(90deg,transparent,#ddd 20%,#ddd 80%,transparent)}

/* second row */
.salon-panel{left:20px;top:492px;width:384px;height:316px;background:var(--panel-light);border-radius:6px}
.salon-title{left:36px;top:510px;font-size:21px;font-family:Arial,sans-serif;color:var(--ink);font-weight:400}
.salon-copy{left:36px;top:539px;width:360px;font-size:12.6px;line-height:18px;font-family:Arial,sans-serif}
.salon-image{left:82px;top:622px;width:310px;height:176px;border-radius:6px;background:linear-gradient(150deg,#cfcfcf,#6b6b6b 60%,#2f2f2f)}
.pos-panel{left:420px;top:492px;width:709px;height:316px;background:var(--panel-dark);border-radius:6px}
.pos-title{left:420px;top:505px;width:709px;text-align:center;font-family:"Didact Gothic",sans-serif;font-size:28px;line-height:36px;color:#fff}
.pos-copy{left:459px;top:616px;width:250px;font-family:"Didact Gothic",sans-serif;font-size:17.5px;line-height:24px;color:#fff}
.pos-image{left:750px;top:597px;width:326px;height:180px;border-radius:4px;background:linear-gradient(135deg,#1f5fa6,#5fa4e0 55%,#cfd8e0)}
.btn-video{left:459px;top:737px;width:172px;height:46px;background:#a0a0a0;color:#fff;font-family:"Didact Gothic",sans-serif;font-size:22px;display:flex;align-items:center;justify-content:space-between;padding:0 12px;border-radius:2px}

/* quote form */
.quote-box{left:20px;top:857px;width:384px;height:291px;border:1px solid var(--line)}
.quote-title{left:172px;top:898px;font-family:"Didact Gothic",sans-serif;font-size:21px;color:var(--red)}
.field-label{left:32px;font-size:13px;color:var(--ink)}
.field{left:174px;width:220px;height:25px;border:1px solid #d5d5d5;background:#fff}
.select{font-size:12px;padding-left:8px;line-height:23px;color:#444}
.quote-submit{left:172px;top:1112px;font-family:"Didact Gothic",sans-serif;font-size:21px;color:var(--red)}

/* wireless */
.wireless-panel{left:420px;top:832px;width:709px;height:316px;background:var(--band);border-radius:8px}
.wireless-title{left:451px;top:850px;font-family:"Didact Gothic",sans-serif;font-size:27px;color:var(--blue);font-weight:400}
.wireless-copy{left:451px;top:889px;width:660px;font-size:12.2px;line-height:15.5px;color:var(--ink)}
.carrier-grid{left:456px;top:988px;display:grid;grid-template-columns:repeat(8,66px);grid-auto-rows:40px;column-gap:16px;row-gap:17px}
.carrier{background:#fff;border-radius:5px;box-shadow:0 1px 3px rgba(0,0,0,.25);display:flex;align-items:center;justify-content:center}
.carrier span{width:44px;height:14px;border-radius:3px;background:#c9c9c9}

/* footer */
.site-footer{left:0;top:1158px;width:1149px;height:42px;background:var(--band-dark);display:flex;align-items:center;justify-content:center;gap:12px;font-size:12.5px;color:var(--ink)}
.copy-mark{width:18px;height:18px;border:1.5px solid #333;border-radius:50%;font-size:12px;line-height:15px;text-align:center}
</style>
</head>
<body>

<header class="abs site-header"></header>
<div class="abs brand"><span class="brand-dot"></span>VendaloFlo.com</div>
<div class="abs phone">888-555-0142</div>
<nav class="abs main-nav">
  <a href="#">Home</a><a href="#">About</a><a href="#">Solutions</a><a href="#">Services</a><a href="#">Equipment</a><a href="#">Contact</a>
</nav>

<div class="abs divider" style="left:180px;top:124px;width:800px"></div>

<section>
  <div class="abs hero-image" role="img" aria-label="Laptop running payment software with credit cards beside it"></div>
  <div class="abs hero-panel"></div>
  <h1 class="abs hero-title">POS Technology, Systems And Solutions</h1>
  <p class="abs hero-copy">No storefront. No problem. Do you have a PC or Laptop connected to the internet?<br>
  Start processing credit card transactions from any computer with an internet connection. Manually process mail and telephone credit&nbsp; card transactions or swipe card via a USB card swiper. Just like a traditional terminal, but with the added flexubility of giving you access from any interne connection in the world.<br>
  There's no hardware to purchase&nbsp; or soft to download. It's flexible, low-cost and trouble free.</p>
  <a class="abs btn btn-terminal">Virtual Treminal</a>
  <a class="abs btn btn-process">Process Payments
    <svg width="22" height="22" viewBox="0 0 22 22"><circle cx="11" cy="11" r="10" fill="#2a5f8f" stroke="#fff" stroke-width="1.5"/><path d="M9 6l5 5-5 5" fill="none" stroke="#fff" stroke-width="2.2"/></svg>
  </a>
  <div class="abs pdf-link">
    <svg width="34" height="36" viewBox="0 0 34 36"><path d="M6 1h16l8 8v26H6z" fill="#fff" stroke="#bbb"/><rect x="2" y="10" width="24" height="12" rx="2" fill="#d9362b"/><path d="M22 1v8h8" fill="#eee" stroke="#bbb"/></svg>
    <div>PDF&nbsp; Details</div>
  </div>
</section>

<div class="abs divider" style="left:140px;top:478px;width:870px"></div>

<section>
  <div class="abs salon-panel"></div>
  <h2 class="abs salon-title">Brenvale Salon</h2>
  <p class="abs salon-copy">software does everything you've come to expect from a salon software POS system - and so much more.<br>The simple touch screen and finger-friendly salon software design will have you moving at salon speed in no time.</p>
  <div class="abs salon-image" role="img" aria-label="Touch screen POS terminal with receipt printer and cash drawer"></div>

  <div class="abs pos-panel"></div>
  <h2 class="abs pos-title">Complet and Affordable POS Solutions<br>for Retail and Hospitality Merchants!</h2>
  <p class="abs pos-copy">Choose from a variety of accessories that are designed specifically with the retail and restaurante environment!</p>
  <div class="abs pos-image" role="img" aria-label="POS accessories: monitor, receipt printer and PIN pad"></div>
  <a class="abs btn-video">View video
    <svg width="26" height="16" viewBox="0 0 26 16"><path d="M1 1l11 7-11 7zM13 1l11 7-11 7z" fill="#2b6fae"/></svg>
  </a>
</section>

<div class="abs divider" style="left:140px;top:818px;width:870px"></div>

<section>
  <div class="abs quote-box"></div>
  <svg class="abs" style="left:90px;top:850px" width="120" height="46" viewBox="0 0 120 46"><path d="M30 0h60v14h28L60 46 2 14h28z" fill="#2f8fd8"/></svg>
  <h3 class="abs quote-title" style="font-weight:400">Get a FREE quote!</h3>
  <label class="abs field-label" style="top:946px">Full name:</label><div class="abs field" style="top:933px"></div>
  <label class="abs field-label" style="top:970px">Email:</label><div class="abs field" style="top:959px"></div>
  <label class="abs field-label" style="top:996px">Phone:</label><div class="abs field" style="top:985px"></div>
  <label class="abs field-label" style="top:1017px">Type of inquires:</label>
  <div class="abs field select" style="top:1010px">Select
    <svg style="position:absolute;right:0;top:0" width="22" height="23" viewBox="0 0 22 23"><rect width="22" height="23" fill="#e5e5e5"/><path d="M6 9h10l-5 6z" fill="#777"/></svg>
  </div>
  <label class="abs field-label" style="top:1090px">Additional information:</label>
  <div class="abs field" style="top:1043px;height:60px"></div>
  <div class="abs quote-submit">Get Quote Now!</div>

  <div class="abs wireless-panel"></div>
  <h2 class="abs wireless-title">Wireless</h2>
  <p class="abs wireless-copy">Prepaid cellular has seen some explosive growth since inception and the total number of prepaid subscribers is continuing to grow. With dozens of national and regional solutions, having all products and all denominations available are imperative in building customer loyalty and recurring traffic. Now Orbanfield offers service for all major national and regional wireless carriers:</p>
  <div class="abs carrier-grid" aria-label="Supported wireless carriers">
    <div class="carrier"><span></span></div><div class="carrier"><span></span></div><div class="carrier"><span></span></div><div class="carrier"><span></span></div>
    <div class="carrier"><span></span></div><div class="carrier"><span></span></div><div class="carrier"><span></span></div><div class="carrier"><span></span></div>
    <div class="carrier"><span></span></div><div class="carrier"><span></span></div><div class="carrier"><span></span></div><div class="carrier"><span></span></div>
    <div class="carrier"><span></span></div><div class="carrier"><span></span></div><div class="carrier"><span></span></div><div class="carrier"><span></span></div>
    <div class="carrier"><span></span></div><div class="carrier"><span></span></div><div class="carrier"><span></span></div><div class="carrier"><span></span></div>
    <div class="carrier"><span></span></div><div class="carrier"><span></span></div><div class="carrier"><span></span></div><div class="carrier"><span></span></div>
  </div>
</section>

<footer class="abs site-footer">
  <span class="copy-mark">c</span>
  <span>Northgate Acceptance Systems Registered Sales Agent for Cardline Payments Inc. Member Bank: Ridgewell Bank N.A., Pine Harbor, CA - Member.FDIC</span>
</footer>

</body>
</html>
```